Corvane Building Company Portfolio Design

I need a full design for a Company Portfolio for a Kuwait based company called Corvane Building Company, WLL. We offer services in Construction ( Supply of Construction Machinery & Construction Material), Contracting (Steel Structure, Furnishing & Finishing) and Smart Solutions (Smart Homes & Smart Parking).

https://www.filtrobay.com/s/qmtpvkadnehzwro/Photos.zip
Updates

This is a Filtro Bay Link containing all our images that can be used in the Company Profile.

One or more of each can be more than enough to describe each product or service we provide.

Target Market(s)

Construction Companies, Engineering & Design Companies, Consultancy firms.

Industry/Entity Type

Construction

Requirements
Must have
• 1) Must allow for further addition & modification.
Nice to have
• 1) External Photos can be used for a better look & resolution.

```html
<!DOCTYPE html>
<html lang="en">
<head>
<meta charset="utf-8">
<title>Corvane Building Company – Portfolio Cover</title>
<link href="https://fonts.googleapis.com/css2?family=Roboto+Condensed:wght@300;400;700&display=swap" rel="stylesheet">
<style>
  :root {
    --bg-top: #a9d3d8;
    --bg-mid: #5fa3ad;
    --bg-bottom: #1d6572;
    --ink: #0e4a56;
    --ink-light: #2b6f7b;
    --white: #ffffff;
    --steel: #6e6258;
    --interior: #d9a27a;
    --hoist: #4a6f95;
    --sky: #9fc4e3;
    --frame: #7e8b96;
    --timber: #c9772e;
  }
  * { margin: 0; padding: 0; box-sizing: border-box; }
  html, body { width: 849px; height: 1200px; overflow: hidden; }
  body { background: var(--bg-bottom); font-family: "Roboto Condensed", sans-serif; }
  .cover {
    position: relative;
    width: 849px; height: 1200px;
    overflow: hidden;
    background:
      radial-gradient(ellipse 520px 420px at 620px 260px, rgba(255,255,255,0.45), rgba(255,255,255,0) 70%),
      linear-gradient(180deg, var(--bg-top) 0%, var(--bg-mid) 55%, var(--bg-bottom) 100%);
  }
  .cover__beam {
    position: absolute; left: -200px; top: 380px;
    width: 1400px; height: 180px;
    background: linear-gradient(180deg, rgba(255,255,255,0), rgba(255,255,255,0.18), rgba(255,255,255,0));
    transform: rotate(-28deg);
  }
  .brand-top {
    position: absolute; top: 84px; left: 0; width: 100%;
    text-align: center;
    font-weight: 700; font-size: 40px; letter-spacing: 6px;
    color: var(--ink);
  }
  .headline {
    position: absolute; right: 60px; top: 205px;
    text-align: right; color: var(--ink);
    line-height: 0.98;
  }
  .headline__light { font-weight: 300; font-size: 60px; color: var(--ink-light); display: block; }
  .headline__bold { font-weight: 700; font-size: 66px; display: block; }
  .headline__big { font-weight: 700; font-size: 84px; display: block; }
  .headline__inline { font-weight: 300; font-size: 52px; color: var(--ink-light); }
  .pie { position: absolute; left: 0; top: 0; }
  .brand-bottom {
    position: absolute; left: 150px; top: 1122px;
    display: flex; align-items: center; gap: 14px;
    color: var(--white); font-weight: 700; font-size: 38px; letter-spacing: 2px;
  }
  .brand-bottom__mark { width: 22px; height: 22px; background: var(--white); }
</style>
</head>
<body>
<main class="cover">
  <div class="cover__beam"></div>

  <div class="brand-top">CORVANE</div>

  <h1 class="headline">
    <span class="headline__light">Leading</span>
    <span class="headline__bold">Construction</span>
    <span class="headline__light">and Trading</span>
    <span class="headline__big">Company</span>
    <span class="headline__bold"><span class="headline__inline">in</span> Kuwait</span>
  </h1>

  <svg class="pie" width="849" height="1200" viewBox="0 0 849 1200">
    <defs>
      <linearGradient id="g-steel" x1="0" y1="0" x2="1" y2="1"><stop offset="0" stop-color="#8a7d70"/><stop offset="1" stop-color="var(--steel)"/></linearGradient>
      <linearGradient id="g-interior" x1="0" y1="0" x2="1" y2="1"><stop offset="0" stop-color="#f1d9c4"/><stop offset="1" stop-color="var(--interior)"/></linearGradient>
      <linearGradient id="g-hoist" x1="0" y1="0" x2="0" y2="1"><stop offset="0" stop-color="#c6d0d8"/><stop offset="1" stop-color="var(--hoist)"/></linearGradient>
      <linearGradient id="g-sky" x1="0" y1="0" x2="0" y2="1"><stop offset="0" stop-color="var(--sky)"/><stop offset="1" stop-color="#e3eef6"/></linearGradient>
      <linearGradient id="g-frame" x1="0" y1="0" x2="1" y2="1"><stop offset="0" stop-color="#b7c3cc"/><stop offset="1" stop-color="var(--frame)"/></linearGradient>
      <linearGradient id="g-timber" x1="0" y1="0" x2="1" y2="1"><stop offset="0" stop-color="#e6a865"/><stop offset="1" stop-color="var(--timber)"/></linearGradient>
    </defs>
    <g stroke="var(--white)" stroke-width="6" stroke-linejoin="round">
      <path role="img" aria-label="Photo: stacked steel beams and construction material" fill="url(#g-steel)" d="M467 770 L467 440 A330 330 0 0 0 233.7 536.7 Z"/>
      <path role="img" aria-label="Photo: finished office interior with reception desk" fill="url(#g-interior)" d="M467 770 L233.7 536.7 A330 330 0 0 0 137 770 Z"/>
      <path role="img" aria-label="Photo: overhead crane hoist in a workshop" fill="url(#g-hoist)" d="M467 770 L137 770 A330 330 0 0 0 233.7 1003.3 Z"/>
      <path role="img" aria-label="Photo: tower crane against the sky at a building site" fill="url(#g-sky)" d="M467 770 L233.7 1003.3 A330 330 0 0 0 467 1100 Z"/>
      <path role="img" aria-label="Photo: steel structure frame under construction" fill="url(#g-frame)" d="M467 770 L467 1100 A330 330 0 0 0 700.3 1003.3 Z"/>
      <path role="img" aria-label="Photo: timber roof framing" fill="url(#g-timber)" d="M467 770 L700.3 1003.3 A330 330 0 0 0 797 770 Z"/>
    </g>
  </svg>

  <div class="brand-bottom">
    <span class="brand-bottom__mark"></span>
    <span class="brand-bottom__name">CORVANE BUILDING</span>
  </div>
</main>
</body>
</html>
```